Letterhead to Prospective Clients

Create a letterhead (word & canva) that I will use to send letters to prospective clients and also include the Coralwood Estate Partners Logo, My Contact Details and Interchangeable "Suburb". Use the same font and colour pallete

Maris Dulworth | "Suburb" Specialist - Redlands & Surrounds
Mobile: 0417 862 095
Email: MD@CoralwoodEstatePartners.com.au

```html
<!DOCTYPE html>
<html lang="en">
<head>
<meta charset="utf-8">
<title>Coralwood Estate Partners — Letterhead</title>
<link rel="stylesheet" href="https://fonts.googleapis.com/css2?family=Montserrat:wght@400;500;600&display=swap">
<style>
  :root {
    --navy: #0c1a3d;
    --sand: #d4a679;
    --sand-soft: #ecd6bf;
    --paper: #ffffff;
    --backdrop: #cdd3d3;
  }
  * { margin: 0; padding: 0; box-sizing: border-box; }
  html, body {
    width: 1200px;
    height: 1027px;
    overflow: hidden;
    background: var(--backdrop);
    font-family: "Montserrat", sans-serif;
  }
  .letterhead {
    position: absolute;
    left: 254px;
    top: 57px;
    width: 654px;
    height: 924px;
    background: var(--paper);
  }
  .brand {
    position: absolute;
    top: 30px;
    left: 0;
    width: 100%;
    text-align: center;
  }
  .brand-name {
    display: block;
    color: var(--navy);
    font-size: 30px;
    font-weight: 400;
    letter-spacing: 3px;
    text-transform: uppercase;
    line-height: 34px;
  }
  .brand-tagline {
    display: block;
    margin-top: 10px;
    color: var(--sand);
    font-size: 6.5px;
    font-weight: 500;
    letter-spacing: 2.4px;
    text-transform: uppercase;
  }
  .divider-ornament {
    position: absolute;
    top: 99px;
    left: 34px;
    width: 586px;
    height: 4px;
    border-radius: 2px;
    background: linear-gradient(90deg, var(--sand-soft), var(--sand), var(--sand-soft));
  }
  .signature {
    position: absolute;
    top: 810px;
    left: 0;
    width: 100%;
    text-align: center;
  }
  .agent-name {
    color: var(--sand);
    font-size: 26px;
    font-weight: 600;
    line-height: 30px;
  }
  .agent-role {
    color: var(--navy);
    font-size: 11.5px;
    font-weight: 500;
    letter-spacing: 0.5px;
    margin-top: 1px;
  }
  .contact-bar {
    position: absolute;
    top: 870px;
    left: 0;
    width: 100%;
    height: 25px;
  }
  .band {
    position: absolute;
    top: 0;
    height: 25px;
    display: flex;
    align-items: center;
    color: #fff;
  }
  .band-phone {
    left: 0;
    width: 331px;
    background: var(--navy);
    clip-path: polygon(0 0, 100% 0, 296px 100%, 0 100%);
    padding-left: 105px;
    font-size: 14px;
    letter-spacing: 1px;
  }
  .band-email {
    left: 311px;
    width: 343px;
    background: var(--sand);
    clip-path: polygon(33px 0, 100% 0, 100% 100%, 0 100%);
    padding-left: 56px;
    font-size: 11.5px;
    letter-spacing: 0.2px;
  }
  .icon {
    width: 15px;
    height: 15px;
    margin-right: 9px;
    flex: none;
  }
</style>
</head>
<body>
  <main class="letterhead">
    <header class="brand">
      <span class="brand-name">Coralwood</span>
      <span class="brand-tagline">Estate Partners</span>
    </header>

    <div class="divider-ornament" role="img" aria-label="Decorative wave ornament divider in sand tone"></div>

    <section class="signature">
      <p class="agent-name">Maris Dulworth</p>
      <p class="agent-role">"Suburb" Specialist - Redlands &amp; Surrounds</p>
    </section>

    <footer class="contact-bar">
      <div class="band band-phone">
        <svg class="icon" viewBox="0 0 16 16" aria-hidden="true">
          <circle cx="8" cy="8" r="8" fill="#fff"/>
          <path d="M5.2 3.8l1.4 1.9-.8 1c.6 1.2 1.4 2 2.6 2.6l1-.8 1.9 1.4-.8 1.5c-3.3-.3-6.4-3.4-6.7-6.7z" fill="#0c1a3d"/>
        </svg>
        <span>0417 862 095</span>
      </div>
      <div class="band band-email">
        <svg class="icon" viewBox="0 0 16 16" aria-hidden="true">
          <circle cx="8" cy="8" r="8" fill="#fff"/>
          <rect x="4" y="5" width="8" height="6" fill="none" stroke="#d4a679" stroke-width="1"/>
          <path d="M4 5l4 3.5L12 5" fill="none" stroke="#d4a679" stroke-width="1"/>
        </svg>
        <span>MD@CoralwoodEstatePartners.com.au</span>
      </div>
    </footer>
  </main>
</body>
</html>
```